Create a Graphic About YOURSELF and PixelHarbor

PixelHarbor would like you (designers) to create an awesome graphic to promote YOURSELF and your profile on PixelHarbor!

Your graphic should communicate your name, your services and should mention PixelHarbor.

The design should be perfect for sharing on Chatterly. Here's an example of what we'd like http://blog.pixelharbor-example.ca/article/333/pixelharbor-launches-3000-hire-me-social-design-contest

Once you submitted your design, we'd love you to share the design ('advertisement') and promote yourself and PixelHarbor to your friends and potential customers. So make your submissions great and get your friends to vote for your design by 'Liking' it on Chatterly!

Prizes:
$1500 - "PixelHarbor Community" prize awarded to the designer with the most Chatterly 'Likes'
5 x $50 for the next 5 'most liked' designs on Chatterly

$1000 - "Hire Me" prize awarded to the designer who receives the most client invites
5 x $50 for the next 5 'most invited' designers

In summary, this is a great opportunity for you to increase your exposure to PixelHarbor customers and win cash prizes. Show off your design skills and get hired by PixelHarbor customers from around the world!

Target Market(s)

Fans, friends and customers of YOU

Industry/Entity Type

Cash

Requirements
Must have
• 1) Include your PixelHarbor user name on the graphic so customers can find you in the PixelHarbor Designer Directory
2) Include the tagline "Hire Me on PixelHarbor.com!" in your graphic design.
3) Share your design's URL on our Chatterly wall at http://chatterly-example.com/pixelharbor and get your friends to 'like' your design.
Nice to have
• 1) Include a tagline that expresses your design approach/philosophy
2) Artwork dimensions: 403 x 403 px
3) You can submit more than 1 design!
Should not have
• You must own the copyright of any images you use including stock imagery.

```html
<!DOCTYPE html>
<html lang="en">
<head>
<meta charset="utf-8">
<title>Hire Me on PixelHarbor</title>
<link rel="stylesheet" href="https://fonts.googleapis.com/css2?family=Roboto:wght@300;400;700;900&family=Roboto+Condensed:wght@700;900&display=swap">
<style>
  :root {
    --paper: #ffffff;
    --ink-dark: #2f2f2f;
    --ink-mid: #6f6f6f;
    --ink-light: #a8a8a8;
    --accent-blue: #1f5f8f;
    --scene-light: #f6f3ea;
    --scene-warm: #f3e2b0;
    --scene-red: #e6b5b5;
  }
  html, body {
    margin: 0;
    padding: 0;
    overflow: hidden;
    background: var(--paper);
  }
  .canvas {
    position: relative;
    width: 1197px;
    height: 1200px;
    background: var(--paper);
    font-family: "Roboto", Arial, sans-serif;
    overflow: hidden;
  }
  .headline {
    position: absolute;
    top: 208px;
    left: 0;
    width: 100%;
    margin: 0;
    text-align: center;
    font-size: 55px;
    letter-spacing: -0.5px;
    line-height: 1;
    white-space: nowrap;
  }
  .headline__strong { color: var(--ink-dark); font-weight: 700; }
  .headline__soft { color: var(--ink-light); font-weight: 400; }

  .scene {
    position: absolute;
    left: 415px;
    top: 290px;
    width: 360px;
    height: 390px;
    border-radius: 18px;
    background: radial-gradient(ellipse at 55% 65%, var(--scene-red) 0%, var(--scene-warm) 35%, var(--scene-light) 75%);
  }
  .scene-label {
    position: absolute;
    left: 788px;
    top: 458px;
    font-size: 31px;
    letter-spacing: -0.8px;
    line-height: 1;
    color: var(--ink-dark);
    white-space: nowrap;
  }
  .scene-label b { font-weight: 900; }
  .scene-label span { font-weight: 300; color: var(--ink-mid); }

  .pitch {
    position: absolute;
    margin: 0;
    line-height: 1;
    letter-spacing: -0.5px;
    white-space: nowrap;
  }
  .pitch--first { top: 718px; left: 0; width: 100%; text-align: center; }
  .pitch--second { top: 780px; left: 556px; }
  .pitch__soft { color: var(--ink-light); font-weight: 400; font-size: 35px; }
  .pitch__loud { color: var(--ink-mid); font-weight: 900; font-size: 66px; }
  .pitch__mid { color: var(--ink-mid); font-weight: 900; font-size: 46px; }
  .pitch__can { color: var(--ink-light); font-weight: 700; font-size: 52px; }
  .pitch__big { color: var(--ink-mid); font-weight: 900; font-size: 98px; }

  .hire {
    position: absolute;
    left: 798px;
    top: 960px;
    text-align: left;
  }
  .hire__tag {
    font-family: "Roboto Condensed", "Arial Narrow", sans-serif;
    font-weight: 900;
    font-size: 54px;
    letter-spacing: -1px;
    line-height: 1;
    color: var(--ink-dark);
  }
  .hire__tag small { font-size: 40px; font-weight: 700; }
  .hire__site,
  .hire__user {
    display: flex;
    align-items: center;
    gap: 10px;
    letter-spacing: -1px;
    white-space: nowrap;
  }
  .hire__site {
    margin-top: 4px;
    font-weight: 700;
    font-size: 40px;
    color: var(--accent-blue);
  }
  .hire__user {
    margin-top: 40px;
    font-weight: 700;
    font-size: 32px;
    color: var(--ink-dark);
  }
  .hire__dot {
    flex: none;
    width: 26px;
    height: 26px;
    border-radius: 50%;
    background: var(--accent-blue);
  }
  .hire__square {
    flex: none;
    width: 24px;
    height: 24px;
    background: var(--ink-dark);
  }
</style>
</head>
<body>
<main class="canvas">
  <h1 class="headline"><span class="headline__strong">I just don't act,</span> <span class="headline__soft">I think different...</span></h1>

  <div class="scene" role="img" aria-label="Illustration: a yellow pencil stabbing a chalk-outline figure lying on the ground, with a red pool of ink like blood"></div>
  <div class="scene-label"><b>graphic</b><span>design</span></div>

  <p class="pitch pitch--first">
    <span class="pitch__soft">if this caught you</span>
    <span class="pitch__loud">attention</span>
    <span class="pitch__soft">imagine</span>
    <span class="pitch__mid">WHAT</span>
  </p>
  <p class="pitch pitch--second">
    <span class="pitch__big">i</span><span class="pitch__can">can</span>
    <span class="pitch__big">DO</span>
    <span class="pitch__soft">for you!</span>
  </p>

  <div class="hire">
    <div class="hire__tag">HIRE<small>meon</small></div>
    <div class="hire__site"><span class="hire__dot"></span>PixelHarbor.com</div>
    <div class="hire__user"><span class="hire__square"></span>clearideagraphics</div>
  </div>
</main>
</body>
</html>
```